Fun Project: Help Make A High Tech Company Look High Tech

Professional Website redesign for IT Maintenance Contract & Asset Management Services Company.

See their website below to understand who they are and what they do.

Note: This is for design only. No coding required. We want to see your ideas for a great website! This project will be a FUN design and not boring like others you may have worked on.

Please let your creative ideas flow. We have given you a ton of info along with videos to help you understand what we are after. However, we WANT your creativity to shine through in your designs!

You will be doing the homepage of this design. If you are chosen as the winner, we will ask for your help with an interior page design. However for the initial phases just the homepage is required.

We are a professional company that has run hundreds of crowdsourced projects on multiple platforms. If you participate in this contest (we hope you do) you can expect great video feedback and consistent feedback. We guarantee that if we know your website design will not be what we are looking for, we will notify you, so you don’t waste your time if there is no chance of you winning.

We respect and recognize this is how you make your living, and we will not play games. We look forward to an awesome contest and awesome website designs.

Design Brief:

We are looking for a fresh and professional new website design for Brightline Fleet Stewards.

Here is their current website: http://brightlinefleetstewards.example/

This company is a high-tech company that serves their clients on many different levels. Please visit their site, read about them a bit so you can understand the products and services that they offer. This information will be very helpful in your design process.

They are in need of a fresh new website that needs to convey trust, professionalism, and high-tech while at the same time having some personality and standing out. We do not want to be boring or look like every other site in our industry.

Here is a video to help explain what we like about the current site and what we don’t like:

CURRENT SITE VIDEO: http://clipvault.example/t/kP4nZr8Q

We want a website that is professional-looking. This website will be looked at by high-end decision makers in many sectors of business. We need the site to reflect very favorably on our company and to showcase our company in the best light.

Here are some examples of other sites in their business that have some things we like:

1. https://www.halvorix.example/ Please watch video to learn what we like and don’t like:

Halvorix Video: http://clipvault.example/t/wD7gHm2L

Our client has said that if they could replace the name, and the proprietary info with their info on this site they would be very happy with the outcome. I know we can do better :)

2. http://pradobyte.example/ Please watch video to learn what we like and don’t like:

Prado Byte Video: http://clipvault.example/t/qR5uVx9Nb

Our client has said that the like the sleekness of their homepage, but overall the site seems too simplistic and generic.

3. http://lanternworksnq.example/ Please watch video to learn what we like and don’t like:

Lantern Works Video: http://clipvault.example/t/z3HyoPa6Wfd

This site is a great example of a site that we would not want. Too simple, to old feeling, to outdated for the times and our industry.

NOTE: We do not want to copy anything outright. We want to learn, model and take their ideas and make them better. We also want you to be flexible and take what we like along with your creativity to make an amazing design.

We do not want templates, themes, or anything like that. We are looking for custom design. If we feel you are just using templates as a way to win, we will just disqualify you.

Here is what we are looking for in more specific terms:

Site structure: We want a horizontal header, horizontal menu, a place for video in the upper left-hand part of the site. We also want columns to help us separate the important parts of our business on the homepage into simple easy to identify parts.

Colors: We like the darker blue that conveys high tech, cyber, IT, servers, etc. You can see examples of the blues that we like in the halvorix video above.

Grays: Gray gives sites a high-tech feel if used right. I think you can see that in the Prado video above.

Deep Purple: Our logo has a deep rich purple to it. This logo and it's colors helps us stand out in our industry. We will be keeping the logo and the colors so please work it into your design.

When looking at colors, please know that the current site and look is NOT what we are aiming for. We are going for a clean and professional look but also a look that is Bold and Vibrant (hence the colors).

Please use complementary colors on the site that blend well together to make an aesthetically pleasing design.

Menu: Horizontal. We like bold and easy to read menu items. Don’t make it small and cluttered.

Site Structure: Clean and easy to navigate. We have a lot of content to display, so we need a clean structure that breaks up the text and content areas.

Images: Please pull images from the current site or use stock footage.. We can always replace the images of course, but if you show them “their own industry” in the new design you will be closer to winning because it will feel more like “them”. We will purchase any images needed for the design once we choose a winner. We prefer Pixmarla Stock and Vendrapix as images sources.

Look and Feel: Professional. Bold. High-End. Business-like. We have already stated many times the feel of this site.

Content Areas: It is a safe bet that if it is on the current site we need it on the new site. So don’t drop anything as it makes it hard to “cut content”. Feel free to arrange it however you see fit though.

What we don't want: We do not want clutter, boring, or templates or themes. We don’t want too cartoony, too cute, or too fancy. We do not want to look like other companies in our industry, and we do not want anything close to our current site. Be creative!

Out of respect to professional designers who are working hard to win if you do not follow this brief, you submit worn out themes, templates, or boring designs you will be eliminated from this contest. We are offering great prize money for this contest, so we expect great visual designs.

Here are some words that we would use that would help describe the type of site that we are looking for:

IT (information technology)
Cyber
Data
High Tech
Servers
Cloud Based
Automation
Silicon Valley
Global IT
Fiber Optic
Virtualization
Data Center
Enterprise Level Services
Storage (Big Data)
Network

We appreciate your interest in this contest. Please let us know if you have any question, need clarification, or any thoughts on this project to share with us. We are eager to work with you if you are interested in this contest.

Thanks!

Target Market(s)

The target market for our products and services is large corportations and divisions of goverment that need our services.

Industry/Entity Type

It Company

Number of Pages Required

1 page

Font styles to use
Sans Serif

Requirements
Must have
• Video integrated into design.
• Follow our brief
• Professional
• Bold
• Clean
Nice to have
• please follow our brief on this.
Should not have
• Clutter
• templates
• themes
• disorginazation

```html
<!DOCTYPE html>
<html lang="en">
<head>
<meta charset="utf-8">
<title>Brightline Fleet Stewards — IT Maintenance &amp; Asset Management</title>
<link href="https://fonts.googleapis.com/css2?family=Open+Sans:wght@400;600;700&family=Poiret+One&display=swap" rel="stylesheet">
<style>
:root{
  --purple:#4b3872;
  --purple-dark:#33244f;
  --purple-light:#6a56a0;
  --ink:#333333;
  --text:#555555;
  --muted:#777777;
  --line:#e2e2e2;
  --panel:#f2f2f2;
  --footer:#2e2e2e;
  --footer-deep:#1f1f1f;
  --white:#ffffff;
}
*{box-sizing:border-box;margin:0;padding:0}
html,body{width:1200px;height:2744px;overflow:hidden;background:var(--white)}
body{font-family:"Open Sans",Arial,sans-serif;color:var(--text)}
.page{position:relative;width:1200px;height:2744px;overflow:hidden}
.abs{position:absolute}
.display{font-family:"Poiret One","Century Gothic",sans-serif;color:var(--purple-dark);font-weight:400;white-space:nowrap}

/* header */
.topline{left:0;top:0;width:1200px;height:4px;background:var(--purple-dark)}
.brand{left:100px;top:48px;display:flex;align-items:center;gap:12px}
.brand-dot{width:26px;height:26px;border-radius:50%;background:var(--purple)}
.brand-name{font-family:"Open Sans",sans-serif;font-size:21px;font-weight:600;color:var(--purple-dark)}
.phone{left:680px;top:50px;font-size:19px;color:var(--ink);display:flex;align-items:center;gap:8px}
.toplinks{left:868px;top:54px;font-size:13.5px;color:var(--ink)}
.toplinks span{margin:0 6px;color:#999}
.nav{left:366px;top:94px;display:flex;gap:0}
.nav a{font-size:14px;font-weight:600;color:var(--ink);text-decoration:none;margin-right:41px;position:relative}
.nav a.active:after{content:"";position:absolute;left:-4px;right:-4px;bottom:-9px;height:2px;background:var(--purple)}
.nav a:last-child{margin-right:0}

/* hero */
.hero{left:0;top:155px;width:1200px;height:518px;background:linear-gradient(180deg,#2d4a86 0%,#6f8fc2 38%,#c8d6ea 70%,#eef2f8 100%)}
.hero-title{left:296px;top:368px;font-size:31px}
.hero-sub{left:300px;top:410px;font-size:15px;color:var(--purple-dark);font-family:"Poiret One",sans-serif}
.hero-arrow{top:392px}

/* welcome */
.welcome{left:99px;top:607px;width:997px;height:326px}
.video{left:152px;top:636px;width:402px;height:227px;border-radius:4px;overflow:hidden;background:#1c1c1c;box-shadow:0 2px 8px rgba(0,0,0,.35)}
.video-still{position:absolute;left:0;top:0;width:402px;height:190px;background:linear-gradient(90deg,#9aa7b6 0%,#c6ccd3 40%,#3b4a3c 70%,#29372b 100%)}
.play{position:absolute;left:168px;top:62px;width:64px;height:64px;border-radius:50%;background:rgba(255,255,255,.55)}
.controls{position:absolute;left:0;top:190px;width:402px;height:37px;background:linear-gradient(#3a3a3a,#111)}
.welcome-title{left:609px;top:654px;font-size:28px}
.welcome-text{left:582px;top:708px;width:482px;font-size:11.4px;line-height:20px;color:var(--text)}
.btn{display:inline-flex;align-items:center;justify-content:center;background:linear-gradient(var(--purple-light),var(--purple-dark));color:var(--white);font-size:12px;border-radius:3px}
.welcome-btn{left:582px;top:827px;width:102px;height:37px}

/* services */
.services{left:0;top:969px;width:1200px;height:664px;background:linear-gradient(90deg,#d5dbe2 0%,#eef1f4 25%,#f7f8fa 50%,#eef1f4 75%,#d5dbe2 100%)}
.section-title{font-size:33px;text-align:center;width:1200px;left:0}
.card{top:1191px;width:224px;height:382px;background:#f4f4f4;box-shadow:0 3px 10px rgba(0,0,0,.12)}
.card-photo{position:absolute;left:37px;top:-75px;width:150px;height:150px;border-radius:50%;border:5px solid var(--white);box-shadow:0 2px 6px rgba(0,0,0,.25)}
.card h3{position:absolute;left:0;top:96px;width:224px;padding:0 14px;font-size:16.5px;font-weight:400;line-height:21px;color:var(--ink)}
.card p{position:absolute;left:0;top:145px;padding:0 14px;font-size:11.6px;line-height:17px;color:var(--text)}
.card ul{position:absolute;left:14px;top:207px;list-style:none;width:200px}
.card li{font-size:11.6px;line-height:15px;margin-bottom:5px;padding-left:16px;position:relative;color:var(--text)}
.card li:before{content:"";position:absolute;left:1px;top:3px;width:5px;height:8px;border-right:2px solid #555;border-bottom:2px solid #555;transform:rotate(40deg)}
.card .btn{position:absolute;left:14px;top:331px;width:102px;height:37px}

/* quote */
.panel{left:99px;width:1004px;background:var(--panel);border:1px solid var(--line)}
.quote{top:1675px;height:156px}
.panel h2{position:absolute;left:62px;font-size:21px;font-family:"Poiret One",sans-serif;color:var(--purple-dark);font-weight:400;white-space:nowrap}
.panel p{position:absolute;left:62px;font-size:12.2px;line-height:21px;color:var(--text)}
.quote-btn{left:883px;top:1748px;width:149px;height:45px;font-size:13px}

/* manufacturers */
.makers{left:137px;top:1968px;width:926px;display:flex;justify-content:space-between;align-items:center}
.maker{font-size:26px;font-weight:700;color:#c8201f}
.maker.dark{color:#222}
.maker.blue{color:#1b5f9e}
.slider-arrow{top:1984px}

/* trademark */
.trademark{top:2087px;height:148px}

/* certification band */
.cert-band{left:0;top:2279px;width:1200px;height:163px;background:#f1f1f1}
.cert-badge{left:207px;top:2300px;width:116px;height:116px;border-radius:50%;background:#1d4e9a;border:6px solid #d7dbe4}
.cert-text{left:349px;top:2348px;font-size:22px;font-family:"Poiret One",sans-serif;color:var(--purple-dark);white-space:nowrap}

/* footer */
.footer{left:0;top:2442px;width:1200px;height:250px;background:var(--footer)}
.footer-bar{left:0;top:2692px;width:1200px;height:52px;background:var(--footer-deep);color:#cfcfcf;font-size:11.5px;text-align:center;line-height:52px}
.fcol{top:2478px}
.fcol h4{font-size:17px;font-weight:600;color:var(--white);letter-spacing:.3px;padding-bottom:6px;border-bottom:1px solid #555;display:inline-block;width:124px;white-space:nowrap}
.fcol ul{list-style:none;margin-top:16px}
.fcol li{font-size:11.3px;color:#dddddd;line-height:19.6px;padding-left:18px;position:relative}
.fcol li:before{content:"";position:absolute;left:2px;top:7px;width:5px;height:5px;border-right:1.5px solid #ccc;border-top:1.5px solid #ccc;transform:rotate(45deg)}
.contact-line{display:flex;gap:14px;color:#e6e6e6;font-size:11.3px;line-height:19px}
.email{width:218px;height:30px;background:var(--white);border-radius:2px;font-size:11px;color:#aaa;padding:7px 10px}
</style>
</head>
<body>
<div class="page">

  <header>
    <div class="abs topline"></div>
    <div class="abs brand"><span class="brand-dot"></span><span class="brand-name">Brightline Fleet Stewards</span></div>
    <div class="abs phone">
      <svg width="16" height="16" viewBox="0 0 24 24"><path fill="#333" d="M6.6 10.8a15.1 15.1 0 0 0 6.6 6.6l2.2-2.2a1 1 0 0 1 1-.25 11.4 11.4 0 0 0 3.6.57 1 1 0 0 1 1 1V20a1 1 0 0 1-1 1A17 17 0 0 1 3 4a1 1 0 0 1 1-1h3.5a1 1 0 0 1 1 1c0 1.25.2 2.45.57 3.6a1 1 0 0 1-.25 1z"/></svg>
      1-800-555-0142
    </div>
    <div class="abs toplinks">Login<span>|</span>Register<span>|</span>Support<span>|</span>Sitemap</div>
    <nav class="abs nav">
      <a class="active">Home</a><a>Services</a><a>Key Features</a><a>About Us</a><a>Our Cloud</a><a>Help Desk</a><a>My Portal</a><a>Contact Us</a>
    </nav>
  </header>

  <section>
    <div class="abs hero" role="img" aria-label="Upward view of glass office towers against a blue sky"></div>
    <h1 class="abs display hero-title">Best-of-breed Solution For IT Maintenance Contract</h1>
    <div class="abs hero-sub">Asset tracking by offering a comprehensive platform</div>
    <svg class="abs hero-arrow" style="left:40px" width="20" height="46" viewBox="0 0 20 46"><path d="M18 2 2 23l16 21" fill="none" stroke="rgba(255,255,255,.7)" stroke-width="2"/></svg>
    <svg class="abs hero-arrow" style="left:1140px" width="20" height="46" viewBox="0 0 20 46"><path d="M2 2l16 21L2 44" fill="none" stroke="rgba(255,255,255,.7)" stroke-width="2"/></svg>
  </section>

  <section>
    <svg class="abs welcome" viewBox="0 0 997 326" width="997" height="326">
      <defs><filter id="cardShadow" x="-5%" y="-5%" width="110%" height="115%"><feDropShadow dx="0" dy="2" stdDeviation="3" flood-opacity=".18"/></filter></defs>
      <path d="M1 1H996V280L498 325 1 280Z" fill="#fff" stroke="#e3e3e3" filter="url(#cardShadow)"/>
    </svg>
    <div class="abs video">
      <div class="video-still" role="img" aria-label="Two technicians reviewing equipment in a server room"></div>
      <div class="play"><svg width="64" height="64" viewBox="0 0 64 64"><path d="M25 19v26l21-13z" fill="#fff"/></svg></div>
      <div class="controls">
        <svg width="402" height="37" viewBox="0 0 402 37">
          <path d="M12 12v13l10-6.5z" fill="#fff"/>
          <text x="30" y="23" fill="#ccc" font-size="8" font-family="Open Sans,sans-serif">1:20</text>
          <rect x="52" y="16" width="216" height="5" rx="2" fill="#555"/>
          <rect x="52" y="16" width="78" height="5" rx="2" fill="#3c8fd0"/>
          <text x="274" y="23" fill="#ccc" font-size="8" font-family="Open Sans,sans-serif">3:12</text>
          <path d="M300 15h4l5-4v14l-5-4h-4z" fill="#3c8fd0"/>
          <rect x="336" y="13" width="22" height="11" rx="2" fill="#444"/>
          <text x="340" y="22" fill="#fff" font-size="8" font-weight="700" font-family="Open Sans,sans-serif">HD</text>
          <path d="M372 12h5M372 12v5M388 12h-5M388 12v5M372 25h5M372 25v-5M388 25h-5M388 25v-5" stroke="#fff" stroke-width="2"/>
        </svg>
      </div>
    </div>
    <h2 class="abs display welcome-title">Welcome To Brightline Fleet Stewards</h2>
    <p class="abs welcome-text">BFS Offers a best-of-breed SaaS solution for consolidating, managing, tracking, and renewing your IT maintenance contracts as well as track your fixed assets. Regardless of your IT hardware brand, age, location, or SLA need, we build a custom solution fit for our client. Our innovative web-based portal and customer service team provides our clients with best-in-class IT service through a single comprehensive solution.</p>
    <a class="abs btn welcome-btn">Read More</a>
  </section>

  <section>
    <div class="abs services" role="img" aria-label="Softly lit rows of data center server racks"></div>
    <h2 class="abs display section-title" style="top:1026px">Our Services</h2>

    <article class="abs card" style="left:115px">
      <div class="card-photo" role="img" aria-label="Technician working at a server rack" style="background:radial-gradient(circle,#6a7c92,#1d2a3c)"></div>
      <h3>Maintance And Warranty Tracking</h3>
      <p>BFS is a powerful web-based tool to track the equipment and software support contracts</p>
      <ul><li>Contract Management Portal</li><li>Flexibility</li><li>Contract Management Portal</li><li>Flexibility</li><li>Automated Notifications</li></ul>
      <a class="btn">Read More</a>
    </article>

    <article class="abs card" style="left:364px">
      <div class="card-photo" role="img" aria-label="Blue lit data center corridor" style="background:radial-gradient(circle,#5f86e0,#10205a)"></div>
      <h3>Asset Management For The Enterprise</h3>
      <p>The BFS platform, as a leading asset management portal for external vendors or customers</p>
      <ul><li>Asset Tracking</li><li>Interface, Component Tracking</li><li>Scalable Yet Affordable</li><li>Integrated</li><li>Cloud Based SaaS</li></ul>
      <a class="btn">Read More</a>
    </article>

    <article class="abs card" style="left:613px">
      <div class="card-photo" role="img" aria-label="Hands holding a tablet in front of network equipment" style="background:radial-gradient(circle,#4f8a9c,#152d3a)"></div>
      <h3>Multi-Platform IT Maintaince Solutions</h3>
      <p>BFS provides a single point of contact for purchasing, managing, consolidating.</p>
      <ul><li>Global Source for IT Maintenance Service Agreements</li><li>Maintenance Service Contract Offerings</li><li>Dedicated BFS Customer Service Team</li></ul>
      <a class="btn">Read More</a>
    </article>

    <article class="abs card" style="left:862px">
      <div class="card-photo" role="img" aria-label="Engineer inspecting a server cabinet" style="background:radial-gradient(circle,#b9bec6,#4a4f58)"></div>
      <h3>We Build a Custom Solution Fit</h3>
      <p>Our innovative web-based portal and customer service team provides our clients with</p>
      <ul><li>Our innovative web-based portal</li><li>Customer service team</li><li>our clients with best-in-class IT service</li></ul>
      <a class="btn">Read More</a>
    </article>
  </section>

  <section>
    <div class="abs panel quote">
      <h2 style="top:40px">Get a quote from Brightline Fleet Stewards</h2>
      <p style="top:78px;width:700px;font-size:11.8px">Lorem Ipsum is simply dummy text of the printing and typesetting industry. Lorem Ipsum has been the industry's standard ever since the 1500s, when an unknown printer took a galley of type and scrambled it to make a type specimen book.</p>
    </div>
    <a class="abs btn quote-btn">Request Quote</a>
  </section>

  <section>
    <h2 class="abs display section-title" style="top:1896px">Manufacturers We Serve</h2>
    <svg class="abs slider-arrow" style="left:62px" width="12" height="22" viewBox="0 0 12 22"><path d="M10 2 2 11l8 9" fill="none" stroke="#aaa" stroke-width="2"/></svg>
    <svg class="abs slider-arrow" style="left:1128px" width="12" height="22" viewBox="0 0 12 22"><path d="M2 2l8 9-8 9" fill="none" stroke="#aaa" stroke-width="2"/></svg>
    <div class="abs makers">
      <span class="maker">Solvane</span>
      <span class="maker">Quillex</span>
      <span class="maker">Koriyu</span>
      <span class="maker dark">Braxmere</span>
      <span class="maker blue">Cyntra</span>
    </div>
  </section>

  <section>
    <div class="abs panel trademark">
      <h2 style="top:40px">Brightline Fleet Stewards (BFS) logos are trademarks of Brightline Fleet Stewards</h2>
      <p style="top:78px;width:880px">Brightline Fleet Stewards (BFS) logos are trademarks of Brightline Fleet Stewards. All other company and product names may be trademarks of their respective companies. While every effort is made to ensure the accuracy of provided information.</p>
    </div>
  </section>

  <section>
    <div class="abs cert-band"></div>
    <div class="abs cert-badge"></div>
    <p class="abs cert-text">Brightline Fleet Stewards (BFS) logos are trademarks of Brightline Fleet Stewards.</p>
  </section>

  <footer>
    <div class="abs footer"></div>
    <div class="abs fcol" style="left:99px">
      <h4>QUICK LINKS</h4>
      <ul><li>Home</li><li>Services</li><li>Key Features</li><li>About Us</li><li>Our Cloud</li><li>My Portal</li><li>Contact Us</li></ul>
    </div>
    <div class="abs fcol" style="left:340px">
      <h4>SITEMAP</h4>
      <ul><li>Veritus oportere</li><li>Finibus Bonorum</li><li>Dignissimos ducimus</li><li>Blanditiis praesentium</li><li>Mollitia animi</li></ul>
    </div>
    <div class="abs fcol" style="left:563px;width:220px">
      <h4 style="width:204px">CONTACT DETAILS</h4>
      <div class="contact-line" style="margin-top:18px">
        <svg width="14" height="18" viewBox="0 0 14 18" style="flex:none"><path d="M7 0a7 7 0 0 1 7 7c0 5-7 11-7 11S0 12 0 7a7 7 0 0 1 7-7z" fill="#fff"/><circle cx="7" cy="7" r="2.6" fill="#2e2e2e"/></svg>
        <span style="font-weight:600">Lorem Ipsum is simply dummy text of the printing and type setting street-395001</span>
      </div>
      <div class="contact-line" style="margin-top:18px;font-size:15px;align-items:center">
        <svg width="14" height="14" viewBox="0 0 24 24" style="flex:none"><path fill="#fff" d="M6.6 10.8a15.1 15.1 0 0 0 6.6 6.6l2.2-2.2a1 1 0 0 1 1-.25 11.4 11.4 0 0 0 3.6.57 1 1 0 0 1 1 1V20a1 1 0 0 1-1 1A17 17 0 0 1 3 4a1 1 0 0 1 1-1h3.5a1 1 0 0 1 1 1c0 1.25.2 2.45.57 3.6a1 1 0 0 1-.25 1z"/></svg>
        +1 415 555 0187
      </div>
    </div>
    <div class="abs fcol" style="left:883px;width:230px">
      <h4 style="width:190px">NEWSLETTER SIGNUP</h4>
      <p style="margin-top:16px;font-size:11.3px;line-height:19px;color:#ddd">Lorem ipsum dolor sit amet, consectetur adipiscing elit.</p>
      <div class="email" style="margin-top:18px">Email address</div>
      <div class="btn" style="margin-top:16px;width:110px;height:37px">Subcribe</div>
    </div>
    <div class="abs footer-bar">Copyright 2015 Brightline Fleet Stewards. All Rights Reserved</div>
  </footer>

</div>
</body>
</html>
```